Brelvo Pizza & Pasta Takeaway Flyer

Our takeaway shop needs a well designed flyer for print and letter box distribution. Design to have a clear list of menu, Specials, contact details. If menu doesn't fit into A4, we won't mind going upto extended A4. I have attached draft copy of our menu and list of item in excel. Please add 5mm Bleed to the flyer.
Flyer will get printed on 115gsm Gloss stock.

```html
<!DOCTYPE html>
<html lang="en">
<head>
<meta charset="utf-8">
<title>Brelvo Pizza &amp; Pasta Takeaway Menu</title>
<link rel="stylesheet" href="https://fonts.googleapis.com/css2?family=Lilita+One&family=Didact+Gothic&display=swap">
<style>
:root{
  --green:#6fae3c;
  --green-soft:rgba(111,174,60,.92);
  --wood-dark:#4e1c0f;
  --wood:#8b3b1e;
  --wood-light:#a5522a;
  --panel:rgba(60,16,10,.42);
  --text:#ffffff;
  --plate:#c9c9cb;
  --logo:#5aa33a;
}
*{box-sizing:border-box;margin:0;padding:0}
html,body{width:1200px;height:636px;overflow:hidden;background:#fff}
.flyer{position:relative;width:1200px;height:636px;overflow:hidden;font-family:"Didact Gothic",sans-serif;color:var(--text)}
.wood-bg{position:absolute;inset:0;background:linear-gradient(90deg,var(--wood-dark),var(--wood) 30%,var(--wood-light) 55%,var(--wood) 80%,var(--wood-dark))}
.pizza-photo{position:absolute;left:0;top:300px;width:300px;height:336px;background:radial-gradient(circle at 40% 50%,#e08a4a,#c0562a 55%,rgba(140,50,25,0) 80%);opacity:.75}
.plate-photo{position:absolute;left:905px;top:400px;width:420px;height:420px;border-radius:50%;background:radial-gradient(circle at 45% 40%,#e2e2e4,var(--plate) 60%,#9c9ca0)}
.col{position:absolute;top:8px;display:flex;flex-direction:column}
.c1{left:0;width:295px}.c2{left:305px;width:290px}.c3{left:603px;width:292px}.c4{left:903px;width:297px}
.head{background:var(--green-soft);font-family:"Lilita One",sans-serif;font-size:31px;line-height:44px;padding:0 8px;letter-spacing:.5px;display:flex;justify-content:space-between;align-items:center}
.head small{font-family:"Didact Gothic",sans-serif;font-size:13px;display:block;line-height:13px;margin-top:-8px;padding-bottom:3px}
.head .tag{font-family:"Didact Gothic",sans-serif;font-size:18px;line-height:18px;text-align:center}
.list{background:var(--panel);padding:4px 8px 6px}
.item{margin-bottom:3px}
.row{display:flex;align-items:baseline;font-size:15.5px;line-height:18px;white-space:nowrap}
.row .leader{flex:1;border-bottom:2px dotted rgba(255,255,255,.85);margin:0 3px;transform:translateY(-3px)}
.desc{font-size:10px;line-height:10px}
.deal .row{justify-content:space-between}
.c1 .main .item{margin-bottom:2px}
.c1 .ribs .item{margin-bottom:9px}
.contact{background:var(--green-soft);padding:4px 6px 8px;margin-top:8px}
.contact .title{font-family:"Lilita One",sans-serif;font-size:22px;line-height:24px}
.contact p{font-size:15px;line-height:15px}
.contact .big{font-size:20px;line-height:24px;margin-top:4px}
.terms{font-size:10.5px;line-height:12px;padding:16px 6px 0}
.terms span{display:block;padding-left:20px;white-space:nowrap}
.brand{position:absolute;left:1040px;top:500px;display:flex;align-items:center;gap:8px;color:var(--logo);font-size:22px}
.brand i{width:26px;height:26px;border-radius:50%;background:var(--logo);display:block}
</style>
</head>
<body>
<div class="flyer">
  <div class="wood-bg" role="img" aria-label="Dark timber plank background"></div>
  <div class="pizza-photo" role="img" aria-label="Photo of a pepperoni pizza"></div>
  <div class="plate-photo" role="img" aria-label="Photo of an empty plate with a fork"></div>

  <section class="col c1">
    <h2 class="head"><div>MAIN<small>[Served with Chips &amp; Garden Salad]</small></div></h2>
    <div class="list main">
      <div class="item"><div class="row">Chicken Schnitzel with Gravy<span class="leader"></span>16</div></div>
      <div class="item"><div class="row">Veal Schnitzel with Gravy<span class="leader"></span>16</div></div>
      <div class="item"><div class="row">Chicken Parmigiana<span class="leader"></span>17</div></div>
      <div class="item"><div class="row">Three Cheese Parmigiana<span class="leader"></span>17</div><p class="desc">Topped with Parmesan, Mozzarella, Bocconcini &amp; Herbs</p></div>
      <div class="item"><div class="row">Hawiian Parmigiana<span class="leader"></span>17</div><p class="desc">Topped with Cheese, Ham, Pineapple &amp; Herbs</p></div>
      <div class="item"><div class="row">Mexican Parmigiana<span class="leader"></span>17</div><p class="desc">Topped with Cheese, Roasted Capsicum, Jalapenos &amp; Herbs</p></div>
      <div class="item"><div class="row">Marinara Parmigiana<span class="leader"></span>19</div><p class="desc">Topped with Cheese, Seafood mix &amp; Herbs</p></div>
      <div class="item"><div class="row">Creamy Garlic Prawn<span class="leader"></span>19</div><p class="desc">Tiger Prawn, Garlic, White Wine, Spices &amp; Herbs Pan fried with Creamy sauce</p></div>
    </div>
    <h2 class="head" style="margin-top:10px">RIBS &amp; WINGS</h2>
    <div class="list ribs">
      <div class="item"><div class="row">Pork Ribs<span class="leader"></span>17</div></div>
      <div class="item"><div class="row">Beef Ribs<span class="leader"></span>15</div></div>
      <div class="item"><div class="row">Buffalo Wings (6 Pcs)<span class="leader"></span>8</div></div>
      <div class="item"><div class="row">BBQ Wings (6 Pcs)<span class="leader"></span>8</div></div>
      <div class="item"><div class="row">Honey Soy wings (6 Pcs)<span class="leader"></span>8</div></div>
      <div class="item"><div class="row">Fried Wings (6 Pcs)<span class="leader"></span>8</div><p class="desc">with Tomato Sauce</p></div>
      <div class="item"><div class="row">Chicken Lollipop (5 Pcs)<span class="leader"></span>8</div><p class="desc">with Lemon Wedges</p></div>
    </div>
  </section>

  <section class="col c2">
    <h2 class="head">THE AB</h2>
    <div class="list">
      <div class="item"><div class="row">AB Chicken<span class="leader"></span>13.95</div><p class="desc">Marinated Chicken,Cheese on Top of Fries, Drizzled with Ranch, BBQ &amp; Garlic Sauce</p></div>
      <div class="item"><div class="row">AB Meat L<span class="leader"></span>13.95</div><p class="desc">Cheese, Pulled Beef, Bacon, Ham on Top of Fries, Drizzled with Ranch, BBQ &amp; Garlic Sauce</p></div>
      <div class="item"><div class="row">AB Combin<span class="leader"></span>13.95</div><p class="desc">Cheese, Chicken, Pulled Beef, Ham on Top of Fries, Drizzled with Ranch, BBQ &amp; Garlic Sauce</p></div>
      <div class="item"><div class="row">AB Veg<span class="leader"></span>13.95</div><p class="desc">Cheese, Tomato, Capsicum, Mushroom, Crumbed Fetta, Pineapple on Top of Fries, Drizzled with Ranch, Tomato &amp; Garlic Sauce</p></div>
      <div class="item"><div class="row">AB Double<span class="leader"></span>11.95</div><p class="desc">Double Cheese on Top of Fries, Drizzled with Ranch, Tomato &amp; Garlic Sauce</p></div>
    </div>
    <h2 class="head" style="margin-top:10px">DESSERT</h2>
    <div class="list">
      <div class="item"><div class="row">Chocolate Sundae<span class="leader"></span>4.95</div></div>
      <div class="item"><div class="row">Nuttoa Calzone<span class="leader"></span>6</div><p class="desc">Calzone filled with Nuttoa &amp; topped with Icing Sugar</p></div>
      <div class="item"><div class="row">Berry Zone<span class="leader"></span>9</div><p class="desc">Nuttoa Calzone filled with Mixed Berry &amp; topped with Icing Sugar</p></div>
      <div class="item"><div class="row">White Valcone<span class="leader"></span>9</div><p class="desc">Calzone filled with White Chocolate &amp; topped with Icing Sugar</p></div>
      <div class="item"><div class="row">Orbo Calzone<span class="leader"></span>9</div><p class="desc">Calzone rolled with Orbo, filled with White Chocolate &amp; topped with Icing Sugar</p></div>
      <div class="item"><div class="row">Tropical Calzone<span class="leader"></span>9</div><p class="desc">Nuttoa Calzone filled with Mango and Pineapple &amp; topped with Icing Sugar</p></div>
    </div>
  </section>

  <section class="col c3">
    <h2 class="head">SALAD</h2>
    <div class="list">
      <div class="item"><div class="row">Garden Salad<span class="leader"></span>6</div><p class="desc">Mixed Leaves, Tomato, Cucumber, Olives, Onion, Cucumber, Pineapple &amp; Italian dressing</p></div>
      <div class="item"><div class="row">Greek Salad<span class="leader"></span>6</div><p class="desc">Mixed Leaves, Tomato, Cucumber, Olives, Onion, Fetta &amp; Dressed with Lemon Juice, Olive Oil, White wine vinegar</p></div>
      <div class="item"><div class="row">Coleslaw<span class="leader"></span>6</div><p class="desc">Red Cabbages, Green Cabbage, Carrot, Onion mixed with Mayonnaise and Lemon</p></div>
      <div class="item"><div class="row">Chicken Ceaser Salad<span class="leader"></span>9</div><p class="desc">Mixed Leaves, Chicken, Crispy Bacon, Croutons, Parmesan Cheese &amp; Ceaser Dressing</p></div>
    </div>
    <h2 class="head" style="margin-top:8px">DRINKS</h2>
    <div class="list">
      <div class="item"><div class="row">Can<span class="leader"></span>2.95</div><p class="desc">Kola, Diet Kola, Kola Zero, Fizzo, Limo</p></div>
      <div class="item"><div class="row">1.25 lit<span class="leader"></span>4.95</div><p class="desc">Kola, Diet Kola, Kola Zero, Fizzo, Limo</p></div>
      <div class="item"><div class="row">Tealo Ice Tea<span class="leader"></span>3.95</div></div>
      <div class="item"><div class="row">Orange Juice<span class="leader"></span>4.50</div></div>
      <div class="item"><div class="row">Ginger Beer<span class="leader"></span>3.95</div></div>
      <div class="item"><div class="row">Mount Fernby Water<span class="leader"></span>2.50</div></div>
      <div class="item"><div class="row">Mava Energy Drink (375 ml)<span class="leader"></span>3.95</div></div>
    </div>
    <div class="contact">
      <h2 class="title">CONTACT DETAILS</h2>
      <p>Brelvo Pizza &amp; Pasta, 112 Harlow Rd, Windmere</p>
      <p class="big">07 3940 2781</p>
      <p class="big">www.brelvo.com.au</p>
    </div>
  </section>

  <section class="col c4">
    <h2 class="head">DINNER PACK<span style="font-family:'Didact Gothic',sans-serif;font-size:28px">$25</span></h2>
    <div class="list">
      <div class="item"><div class="row">Pizza Pack</div><p class="desc">Cheesy Garlic Bread, Any Large Pizza (Excl Premium range), Any Dessert or 1.25 lit</p></div>
      <div class="item"><div class="row">Pasta Pack</div><p class="desc">Curly Fries, Any Pasta, Any Dessert or 1.25 lit</p></div>
      <div class="item"><div class="row">Parmi Pack</div><p class="desc">Chips, Any Parmigiana, Any Dessert or 1.25 lit</p></div>
      <div class="item"><div class="row">Ribs &amp; Wings Pack</div><p class="desc">Chips, Any Wings, Ribs (Pork or Beef)</p></div>
    </div>
    <h2 class="head" style="margin-top:8px">DEALS<span class="tag">FREE DELIVERY<br>$40 and Over</span></h2>
    <div class="list">
      <div class="item deal"><div class="row">Party Deal<span>$54.95</span></div><p class="desc">3 Large Pizza or Pasta, 2 Garlic Bread &amp; 1.25 lit Drink</p></div>
      <div class="item deal"><div class="row">Family Deal<span>$39.95</span></div><p class="desc">2 Large Pizza or Pasta, 2 Garlic Bread, 1.25 lit drink</p></div>
      <div class="item deal"><div class="row">Couple Deal<span>$24.95</span></div><p class="desc">1 Family Pizza, 1 Garlic Bread, 1.25 lit Drink</p></div>
      <div class="item deal"><div class="row">Single Deal<span>$19.95</span></div><p class="desc">1 Large Pizza or Pasta, 1 Garlic Bread, 1 can drink</p></div>
      <div class="item deal"><div class="row">Small Deal<span>$14.95</span></div><p class="desc">1 Small Pizza, 1 Garlic Bread, 1 can drink - $14.95</p></div>
    </div>
    <p class="terms">Terms &amp; Condition:<span>(Large Pizza Excludes Premium &amp; Seafood range, One</span></p>
  </section>

  <div class="brand"><i></i>Brelvo Pizza &amp; Pasta</div>
</div>
</body>
</html>
```